Management consultant needs to update look of website

Currently I have a great word press website but it needs an updated look. I have new text for the site in the attached word document. I also have a list of websites whose design, look, and organization i like as a guide for the designer. The final design should be simple, strong, clear, and project the idea that my brand is a powerful authority in this space. Current site = www.brookfernadvisory.com

Target Market(s)

company owners / executives

Industry/Entity Type

Management Consulting

Number of Pages Required

3 page

Font styles to use
Serif

Colors

Designer to choose colors to be used in the design.

Requirements
Must have
• a simple and clear design and message. professional look. easy navigation. responsive to mobile devices. an easily implemented wordpress theme OR squarespace. use of my logo colors. though I am open to changing to a deep navy or charcoal logo image. source file uploaded.
Nice to have
• i like the cover photo and logo watermark on my current homepage. i like the google map with my logo on the current contact page. i like the animation as well. a great blend of the current site and something that is more seamless.

```html
<!DOCTYPE html>
<html lang="en">
<head>
<meta charset="utf-8">
<title>Brookfern Advisory</title>
<link rel="stylesheet" href="https://fonts.googleapis.com/css2?family=Cormorant+Garamond:wght@500;600&family=Montserrat:wght@400;600;700&display=swap">
<style>
  :root {
    --gold: #c9a548;
    --gold-soft: #d8bd72;
    --ink: #2b2b2b;
    --body: #6f6f6f;
    --muted: #9a9a9a;
    --panel: #f1f1f1;
    --white: #ffffff;
    --line: #e6e6e6;
    --teal: #2ec4a0;
    --serif: "Cormorant Garamond", Georgia, serif;
    --sans: "Montserrat", Arial, sans-serif;
  }
  * { box-sizing: border-box; margin: 0; padding: 0; }
  html, body { width: 1200px; height: 2894px; overflow: hidden; background: var(--white); }
  body { position: relative; font-family: var(--sans); color: var(--body); }

  .site-header { position: absolute; top: 0; left: 0; width: 1200px; height: 93px; background: var(--white); }
  .brand { position: absolute; left: 77px; top: 24px; display: flex; align-items: center; gap: 14px; }
  .brand-dot { width: 44px; height: 44px; border-radius: 50%; background: var(--gold); }
  .brand-name { font-family: var(--serif); font-weight: 600; font-size: 26px; color: var(--gold); letter-spacing: 1px; text-transform: uppercase; }
  .main-nav { position: absolute; top: 38px; left: 720px; display: flex; gap: 0; }
  .main-nav a { font-size: 14px; color: #444; text-decoration: none; letter-spacing: .5px; margin-right: 25px; }
  .main-nav a.active { color: var(--gold); }

  .hero-photo { position: absolute; top: 93px; left: 0; width: 1200px; height: 543px;
    background: linear-gradient(120deg, #3a3833 0%, #5d574d 40%, #48443e 70%, #2e2d2b 100%); }

  .intro { position: absolute; top: 636px; left: 0; width: 1200px; height: 417px; background: var(--white); }
  .intro-photo { position: absolute; right: 0; top: 0; width: 600px; height: 417px;
    background: linear-gradient(90deg, #ffffff 0%, #eeeeee 35%, #e2e2e2 70%, #d9d9d9 100%); }
  .intro-text { position: absolute; left: 79px; top: 55px; width: 580px; }
  .intro h1 { font-family: var(--serif); font-weight: 500; font-size: 38px; line-height: 46px; color: var(--gold); margin-bottom: 22px; }
  .intro p { font-size: 13px; line-height: 25px; margin-bottom: 14px; }

  .testimonials { position: absolute; top: 1053px; left: 0; width: 1200px; height: 1030px; background: var(--panel); }
  .section-title { font-family: var(--serif); font-weight: 500; font-size: 48px; letter-spacing: 1px; color: var(--gold); text-align: center; position: absolute; left: 0; width: 1200px; }
  .testimonials .section-title { top: 42px; }
  .card { position: absolute; width: 239px; height: 230px; background: var(--white); text-align: center; padding: 62px 18px 0; }
  .card-quote { position: absolute; top: -16px; left: 88px; width: 62px; height: 48px; }
  .card-name { font-weight: 700; font-size: 15px; color: var(--ink); margin-bottom: 12px; letter-spacing: .3px; }
  .card-text { font-size: 12.5px; line-height: 25px; color: var(--muted); }

  .clients { position: absolute; top: 2083px; left: 0; width: 1200px; height: 512px; background: var(--white); }
  .clients .section-title { top: 48px; }
  .logo-grid { position: absolute; left: 77px; top: 122px; width: 1046px; height: 312px; display: grid; grid-template-columns: repeat(5, 1fr); grid-template-rows: repeat(3, 1fr); }
  .logo-cell { display: flex; align-items: center; justify-content: center; gap: 10px; border-right: 1px solid var(--line); border-bottom: 1px solid var(--line); }
  .logo-cell:nth-child(5n) { border-right: none; }
  .logo-cell:nth-child(n+11) { border-bottom: none; }
  .logo-mark { width: 28px; height: 28px; background: #d6d6d6; }
  .logo-name { font-weight: 600; font-size: 22px; line-height: 20px; color: #b5b5b5; }
  .logo-cell.featured .logo-mark { background: var(--teal); }
  .logo-cell.featured .logo-name { color: #222; }

  .signup { position: absolute; top: 2595px; left: 0; width: 1200px; height: 299px; background: var(--panel); text-align: center; }
  .signup h2 { font-family: var(--serif); font-weight: 500; font-size: 38px; line-height: 46px; color: var(--gold); margin-top: 55px; }
  .signup p { font-size: 13px; line-height: 24px; width: 600px; margin: 10px auto 0; }
  .signup-form { position: absolute; left: 116px; top: 233px; display: flex; gap: 9px; }
  .field { width: 249px; height: 46px; border: 2px solid var(--gold-soft); border-radius: 23px; background: var(--white); font-family: var(--sans); font-size: 13px; color: #777; text-align: left; padding: 0 22px; line-height: 42px; }
  .submit { width: 414px; height: 46px; margin-left: 5px; border-radius: 23px; background: var(--gold); color: var(--white); font-family: var(--serif); font-weight: 600; font-size: 20px; letter-spacing: 1px; line-height: 46px; text-transform: uppercase; }
</style>
</head>
<body>

<header class="site-header">
  <div class="brand"><span class="brand-dot"></span><span class="brand-name">Brookfern Advisory</span></div>
  <nav class="main-nav">
    <a class="active" href="#">HOME</a>
    <a href="#">ABOUT</a>
    <a href="#">SERVICES</a>
    <a href="#">ARTICLES</a>
    <a href="#">CONTACT</a>
  </nav>
</header>

<div class="hero-photo" role="img" aria-label="Team meeting in a bright open-plan office, darkened as a cover photo"></div>

<section class="intro">
  <div class="intro-photo" role="img" aria-label="Hands typing on a laptop on a white desk"></div>
  <div class="intro-text">
    <h1>Great Companies Succeed by Investing<br>in the Right People</h1>
    <p>It’s no secret that long-term business success requires a smart investment in the right people for your company. And yet, knowing how to cultivate a strong staff and keep them focused on the road ahead can be challenging for even the savviest organizational leaders and human resource executives.</p>
    <p>I’m Dr. Elena Marsh and I want to help business owners, leaders, and HR teams understand how to identify, develop, and retain talented professionals who can take your success to the next level.</p>
  </div>
</section>

<svg width="0" height="0" style="position:absolute">
  <defs>
    <g id="quote-icon" fill="#c9a548">
      <path d="M2 6 h24 v22 c0 10 -6 17 -16 19 l-2 -6 c5 -2 8 -6 8 -11 h-14 z"/>
      <path d="M34 6 h24 v22 c0 10 -6 17 -16 19 l-2 -6 c5 -2 8 -6 8 -11 h-14 z"/>
    </g>
  </defs>
</svg>

<section class="testimonials">
  <h2 class="section-title">TESTIMONIALS</h2>

  <div class="card" style="left:212px;top:137px"><svg class="card-quote" viewBox="0 0 62 48"><use href="#quote-icon"/></svg><div class="card-name">NAME SURNAME</div><div class="card-text">Lorem Ipsum is simply dummy text of the printing and typesetting industry. Lorem Ipsum has been the industry's standard.</div></div>
  <div class="card" style="left:480px;top:137px"><svg class="card-quote" viewBox="0 0 62 48"><use href="#quote-icon"/></svg><div class="card-name">NAME SURNAME</div><div class="card-text">Lorem Ipsum is simply dummy text of the printing and typesetting industry. Lorem Ipsum has been the industry's standard.</div></div>
  <div class="card" style="left:748px;top:137px"><svg class="card-quote" viewBox="0 0 62 48"><use href="#quote-icon"/></svg><div class="card-name">NAME SURNAME</div><div class="card-text">Lorem Ipsum is simply dummy text of the printing and typesetting industry. Lorem Ipsum has been the industry's standard.</div></div>

  <div class="card" style="left:212px;top:430px"><svg class="card-quote" viewBox="0 0 62 48"><use href="#quote-icon"/></svg><div class="card-name">NAME SURNAME</div><div class="card-text">Lorem Ipsum is simply dummy text of the printing and typesetting industry. Lorem Ipsum has been the industry's standard.</div></div>
  <div class="card" style="left:480px;top:430px"><svg class="card-quote" viewBox="0 0 62 48"><use href="#quote-icon"/></svg><div class="card-name">NAME SURNAME</div><div class="card-text">Lorem Ipsum is simply dummy text of the printing and typesetting industry. Lorem Ipsum has been the industry's standard.</div></div>
  <div class="card" style="left:748px;top:430px"><svg class="card-quote" viewBox="0 0 62 48"><use href="#quote-icon"/></svg><div class="card-name">NAME SURNAME</div><div class="card-text">Lorem Ipsum is simply dummy text of the printing and typesetting industry. Lorem Ipsum has been the industry's standard.</div></div>

  <div class="card" style="left:77px;top:718px"><svg class="card-quote" viewBox="0 0 62 48"><use href="#quote-icon"/></svg><div class="card-name">NAME SURNAME</div><div class="card-text">Lorem Ipsum is simply dummy text of the printing and typesetting industry. Lorem Ipsum has been the industry's standard.</div></div>
  <div class="card" style="left:345px;top:718px"><svg class="card-quote" viewBox="0 0 62 48"><use href="#quote-icon"/></svg><div class="card-name">NAME SURNAME</div><div class="card-text">Lorem Ipsum is simply dummy text of the printing and typesetting industry. Lorem Ipsum has been the industry's standard.</div></div>
  <div class="card" style="left:615px;top:718px"><svg class="card-quote" viewBox="0 0 62 48"><use href="#quote-icon"/></svg><div class="card-name">NAME SURNAME</div><div class="card-text">Lorem Ipsum is simply dummy text of the printing and typesetting industry. Lorem Ipsum has been the industry's standard.</div></div>
  <div class="card" style="left:883px;top:718px"><svg class="card-quote" viewBox="0 0 62 48"><use href="#quote-icon"/></svg><div class="card-name">NAME SURNAME</div><div class="card-text">Lorem Ipsum is simply dummy text of the printing and typesetting industry. Lorem Ipsum has been the industry's standard.</div></div>
</section>

<section class="clients">
  <h2 class="section-title">LOGOS</h2>
  <div class="logo-grid">
    <div class="logo-cell"><span class="logo-mark"></span><span class="logo-name">company<br>name</span></div>
    <div class="logo-cell"><span class="logo-mark"></span><span class="logo-name">company<br>name</span></div>
    <div class="logo-cell"><span class="logo-mark"></span><span class="logo-name">company<br>name</span></div>
    <div class="logo-cell"><span class="logo-mark"></span><span class="logo-name">company<br>name</span></div>
    <div class="logo-cell"><span class="logo-mark"></span><span class="logo-name">company<br>name</span></div>
    <div class="logo-cell"><span class="logo-mark"></span><span class="logo-name">company<br>name</span></div>
    <div class="logo-cell"><span class="logo-mark"></span><span class="logo-name">company<br>name</span></div>
    <div class="logo-cell"><span class="logo-mark"></span><span class="logo-name">company<br>name</span></div>
    <div class="logo-cell featured"><span class="logo-mark"></span><span class="logo-name">company<br>name</span></div>
    <div class="logo-cell"><span class="logo-mark"></span><span class="logo-name">company<br>name</span></div>
    <div class="logo-cell"><span class="logo-mark"></span><span class="logo-name">company<br>name</span></div>
    <div class="logo-cell"><span class="logo-mark"></span><span class="logo-name">company<br>name</span></div>
    <div class="logo-cell"><span class="logo-mark"></span><span class="logo-name">company<br>name</span></div>
    <div class="logo-cell"><span class="logo-mark"></span><span class="logo-name">company<br>name</span></div>
    <div class="logo-cell"><span class="logo-mark"></span><span class="logo-name">company<br>name</span></div>
  </div>
</section>

<section class="signup">
  <h2>Learn to Inspire Employees and Unlock<br>Their Maximum Potential</h2>
  <p>If you’re struggling to connect with today’s employees and you need to develop a better way to lead them, I want to help you become the very best leader possible.</p>
  <div class="signup-form">
    <div class="field">Name</div>
    <div class="field">Email</div>
    <div class="submit">Download Free Information</div>
  </div>
</section>

</body>
</html>
```